Vorlan cards

I am in the auto motive, transportation business I would like a business card that is Something cool, modern edgy, having to do with car culture. I offer towing service for high and exotic cars. I also provide towing for collisions and car accidents. I offer open and enclosed transport nationwide.

Target Market(s)

Car culture people high end auto collectors

Industry/Entity Type

Towing car carrier

Contact Information for Business Card

My company colors black yellow and silver

Font styles to use
Serif

```html
<!DOCTYPE html>
<html lang="en">
<head>
<meta charset="UTF-8">
<title>Vorlan Business Card</title>
<link href="https://fonts.googleapis.com/css2?family=Arvo:wght@400;700&family=Lato:wght@400;700&display=swap" rel="stylesheet">
<style>
  :root {
    --stage: #2b2b2b;
    --card: #1b1b1b;
    --card-back: #1e1e1e;
    --yellow: #f2d43a;
    --white: #f1f1f1;
    --silver: #c9c9c9;
    --emboss: #121212;
  }
  html, body {
    margin: 0;
    width: 1200px;
    height: 800px;
    overflow: hidden;
    background: var(--stage);
  }
  .stage {
    width: 1200px;
    height: 800px;
    display: flex;
    flex-direction: column;
    align-items: center;
    justify-content: center;
    gap: 40px;
  }
  .card {
    position: relative;
    width: 600px;
    height: 343px;
    border-radius: 22px;
    background: var(--card);
    box-shadow: 0 4px 0 var(--yellow), 0 14px 24px rgba(0,0,0,.45);
    overflow: hidden;
  }
  .card--back { background: var(--card-back); }

  .brand {
    position: absolute;
    top: 42px;
    right: 48px;
    display: flex;
    align-items: center;
    gap: 12px;
  }
  .brand__mark {
    width: 16px;
    height: 16px;
    background: var(--yellow);
  }
  .brand__name {
    font-family: "Arvo", serif;
    font-weight: 700;
    font-size: 40px;
    letter-spacing: 2px;
    color: var(--yellow);
  }

  .identity {
    position: absolute;
    left: 56px;
    top: 148px;
  }
  .identity__name {
    font-family: "Arvo", serif;
    font-size: 30px;
    letter-spacing: 1px;
    color: var(--yellow);
    margin: 0;
  }
  .identity__title {
    font-family: "Lato", sans-serif;
    font-size: 17px;
    color: var(--white);
    margin: 4px 0 0 2px;
  }

  .divider {
    position: absolute;
    left: 58px;
    right: 40px;
    top: 226px;
    height: 2px;
    background: var(--yellow);
  }

  .contacts {
    position: absolute;
    left: 56px;
    top: 242px;
    margin: 0;
    padding: 0;
    list-style: none;
    font-family: "Lato", sans-serif;
    color: var(--white);
  }
  .contacts__item {
    display: flex;
    align-items: center;
    gap: 12px;
    height: 26px;
    font-size: 15px;
    letter-spacing: .5px;
  }
  .contacts__item--phone { font-size: 19px; }
  .contacts__icon { width: 14px; height: 14px; fill: var(--yellow); flex: none; }

  .back-brand {
    position: absolute;
    inset: 0;
    display: flex;
    align-items: center;
    justify-content: center;
    font-family: "Arvo", serif;
    font-weight: 700;
    font-size: 84px;
    letter-spacing: 4px;
    color: var(--emboss);
  }
</style>
</head>
<body>
<main class="stage">
  <section class="card card--front">
    <div class="brand">
      <span class="brand__mark"></span>
      <span class="brand__name">VORLAN</span>
    </div>

    <div class="identity">
      <h1 class="identity__name">DEAN CALLOWAY</h1>
      <p class="identity__title">Managing Director</p>
    </div>

    <div class="divider"></div>

    <ul class="contacts">
      <li class="contacts__item contacts__item--phone">
        <svg class="contacts__icon" viewBox="0 0 24 24"><path d="M6.6 10.8a15.1 15.1 0 0 0 6.6 6.6l2.2-2.2c.3-.3.7-.4 1-.2 1.1.4 2.3.6 3.6.6.6 0 1 .4 1 1V20c0 .6-.4 1-1 1A17 17 0 0 1 3 4c0-.6.4-1 1-1h3.5c.6 0 1 .4 1 1 0 1.3.2 2.5.6 3.6.1.3 0 .7-.2 1z"/></svg>
        555-204-7316
      </li>
      <li class="contacts__item">
        <svg class="contacts__icon" viewBox="0 0 24 24"><path d="M2 5h20v14H2zm2 2v.5l8 5 8-5V7l-8 5z"/></svg>
        calloway@vorlantow.com
      </li>
      <li class="contacts__item">
        <svg class="contacts__icon" viewBox="0 0 24 24"><path d="M12 2a10 10 0 1 0 0 20 10 10 0 0 0 0-20zm6.9 6h-3a15 15 0 0 0-1.3-3.9A8 8 0 0 1 18.9 8zM12 4c.8 1.2 1.5 2.5 1.9 4h-3.8c.4-1.5 1.1-2.8 1.9-4zM4.3 14a8 8 0 0 1 0-4h3.4a16 16 0 0 0 0 4zm.8 2h3a15 15 0 0 0 1.3 3.9A8 8 0 0 1 5.1 16zm3-8h-3a8 8 0 0 1 4.3-3.9C8.8 5.3 8.4 6.6 8.1 8zM12 20c-.8-1.2-1.5-2.5-1.9-4h3.8c-.4 1.5-1.1 2.8-1.9 4zm2.3-6H9.7a14.7 14.7 0 0 1 0-4h4.6a14.7 14.7 0 0 1 0 4zm.3 5.9c.6-1.2 1-2.5 1.3-3.9h3a8 8 0 0 1-4.3 3.9zm1.7-5.9a16 16 0 0 0 0-4h3.4a8 8 0 0 1 0 4z"/></svg>
        www.vorlantow.com
      </li>
    </ul>
  </section>

  <section class="card card--back">
    <div class="back-brand">VORLAN</div>
  </section>
</main>
</body>
</html>
```